Web Design Project

We need a website design for a new website. The site will have two parts, a sales and marketing site (nothing exists at present) and an online business application, which is under construction.
The sales and marketing site needs a top level menu, and area to log into or sign up to the online applciation. Other than that we are open to suggestions.
The onlne applciations needs a similar look/feel to the marketing site and it's design needs to incorporate the following parts:
- grids
- settings page
- pop up boxes
- error messages
Please create an account on the development site at http://vorlindesk.hostpad.net to see waht functionality needs to be incorporated in the design. Needs to be viewed in FireFox.
The logo we have chosen for the site has been uploaded, please ensure all designs fit with this. I have no problems if you wish to make alterations to the logo.
- Design for both the marketing site and online application.

```html
<!DOCTYPE html>
<html lang="en">
<head>
<meta charset="utf-8">
<title>vorlindesk – Add Expenses</title>
<link href="https://fonts.googleapis.com/css2?family=Noto+Sans:wght@400;700&family=Arimo:wght@400&display=swap" rel="stylesheet">
<style>
  :root{
    --blue:#1b6db3;
    --blue-dark:#115a9c;
    --blue-light:#2f86cc;
    --link:#1f6fb8;
    --green:#6ec22e;
    --green-bright:#9be23a;
    --panel:#f3f3f3;
    --line:#c9d6e6;
    --text:#333;
    --muted:#666;
    --red:#e8201a;
    --save:#1679c4;
  }
  *{box-sizing:border-box;margin:0;padding:0}
  html,body{width:1200px;height:757px;overflow:hidden;background:#fff}
  body{position:relative;font-family:"Noto Sans",sans-serif;color:var(--text)}
  .topbar{position:absolute;left:0;top:0;width:1200px;height:43px;background:linear-gradient(#2a7fc4,var(--blue-dark))}
  .topbar .company{position:absolute;left:713px;top:12px;font-size:15px;color:#fff}
  .topbar .company b{font-weight:400;color:var(--green-bright)}
  .topbar .welcome{position:absolute;left:1005px;top:10px;font-size:15px;color:#fff}
  .topbar .welcome b{font-weight:400;font-size:18px;color:var(--green-bright)}
  .brand-tab{position:absolute;left:87px;top:31px;width:318px;height:102px;background:#fff;border-radius:0 0 50% 50% / 0 0 22% 22%;box-shadow:0 2px 6px rgba(0,0,0,.3)}
  .brand-tab .brand{position:absolute;left:22px;top:20px;display:flex;align-items:center;gap:10px;font-size:40px;font-weight:700;color:var(--green);letter-spacing:-1px}
  .brand-tab .brand i{display:block;width:26px;height:26px;background:var(--blue)}
  .account-links{position:absolute;right:45px;top:54px;font-size:16px;color:var(--link)}
  .account-links span{margin:0 8px;color:var(--link)}
  .main-nav{position:absolute;left:478px;top:144px;width:679px;height:42px;border:2px solid #dedede;border-radius:22px;background:#fff;box-shadow:0 1px 3px rgba(0,0,0,.15);display:flex;align-items:center;padding-left:20px;font-size:13px;color:#555}
  .main-nav a{color:#555;text-decoration:none}
  .main-nav a.active{color:var(--link)}
  .main-nav .sep{margin:0 11px}
  .rule{position:absolute;left:0;top:198px;width:1200px;height:4px;background:#e6e6e6}
  .band{position:absolute;left:0;top:204px;width:1200px;height:300px;background:linear-gradient(90deg,var(--blue-dark),var(--blue-light) 50%,var(--blue-dark))}
  .card{position:absolute;left:43px;top:214px;width:1114px;height:453px;background:#fff;box-shadow:0 0 6px rgba(0,0,0,.25);padding:10px 9px 7px}
  .card-body{height:100%;background:var(--panel)}
  .card-head{height:44px;background:var(--green);display:flex;align-items:center;justify-content:space-between;padding:0 16px 0 10px;color:#fff}
  .card-head h1{font-size:17px;font-weight:700}
  .card-head .counts{font-size:15px;color:#1f2e10}
  .card-head .counts span{margin:0 16px}
  .empty-note{position:absolute;left:61px;top:283px;font-size:15px;color:#222}
  .add-row{position:absolute;left:63px;top:316px;display:flex;align-items:center;gap:10px;font-size:15px;color:var(--muted)}
  .pill-select{width:206px;height:33px;border:1px solid #ccc;border-radius:17px;background:linear-gradient(#fff,#e9e9e9);display:flex;align-items:center;justify-content:space-between;padding:0 6px 0 24px;font-size:12px;color:#666}
  .pill-select svg{width:18px;height:18px}
  .grid{position:absolute;left:52px;top:366px;width:1096px;height:211px;border-collapse:collapse;background:#fff;font-size:12px}
  .grid th{height:45px;text-align:left;font-weight:400;font-size:15px;color:var(--link);border-bottom:2px solid #e1e1e1;padding-left:13px}
  .grid td{border-right:1px solid var(--line);vertical-align:top;padding-top:34px}
  .grid td:last-child{border-right:0}
  .grid{outline:1px solid #ddd}
  .btn{display:block;border-radius:4px;color:#fff;font-size:12px;text-align:center;line-height:22px;height:22px}
  .btn-date{width:69px;margin:0 0 4px 14px;background:var(--save)}
  .box{border:1px solid #ccc;background:#fff;height:22px;display:block}
  .date-box{width:70px;margin-left:14px;height:24px}
  .mini-select{display:inline-flex;align-items:center;justify-content:space-between;height:20px;border:1px solid #bbb;background:#fff;padding:0 5px;font-size:12px;color:#555}
  .mini-select::after{content:"";border:4px solid transparent;border-top:5px solid #222;margin-top:5px;margin-left:6px}
  .desc{position:relative;color:#555}
  .desc .f{position:absolute;font-size:12px}
  .desc h2{position:absolute;left:4px;top:12px;font-size:14px;font-weight:700;color:#666}
  .check{display:inline-block;width:13px;height:13px;border:1px solid #888;background:#f8f8f8}
  .browse{display:inline-block;height:23px;line-height:21px;padding:0 8px;border:1px solid #888;border-radius:3px;background:linear-gradient(#fafafa,#ddd);font-size:12px;color:#222}
  .btn-save{width:70px;margin:0 auto 7px;background:var(--save)}
  .btn-cancel{width:70px;margin:0 auto;background:var(--red)}
  .footer-links{position:absolute;left:52px;top:685px;font-family:"Arimo",sans-serif;font-size:13px;color:#222;line-height:20px}
  .follow{position:absolute;left:896px;top:694px;font-family:"Arimo",sans-serif;font-size:15px;color:#222}
  .social{position:absolute;top:685px;width:38px;height:38px;border-radius:50%;background:radial-gradient(#fff,#e3e3e3);box-shadow:0 1px 3px rgba(0,0,0,.35)}
</style>
</head>
<body>
  <header class="topbar">
    <div class="company">Company Name : <b>Brightform</b></div>
    <div class="welcome">Welcome <b>Leo 3187</b></div>
  </header>
  <div class="brand-tab"><div class="brand"><i></i>vorlindesk</div></div>
  <nav class="account-links">Edit Profile <span>|</span>Change Password <span>|</span> Logout</nav>
  <nav class="main-nav">
    <a class="active">ADD EXPENSE</a><span class="sep">|</span>
    <a>EXISTING EXPENSE</a><span class="sep">|</span>
    <a>CLAIM MANAGEMENT</a><span class="sep">|</span>
    <a>SETTINGS</a><span class="sep">|</span>
    <a>USER MANAGEMENT</a>
  </nav>
  <div class="rule"></div>
  <div class="band"></div>

  <main class="card">
    <div class="card-body">
      <div class="card-head">
        <h1>ADD EXPENSES</h1>
        <div class="counts">Unclaimed (0)<span>|</span>Rejected (0)</div>
      </div>
    </div>
  </main>

  <p class="empty-note">There are no unclaimed expenses to display</p>
  <div class="add-row">Add Expense
    <div class="pill-select">Add Expense
      <svg viewBox="0 0 18 18"><circle cx="9" cy="9" r="9" fill="#111"/><path d="M5 7l4 4 4-4" stroke="#fff" stroke-width="2" fill="none"/></svg>
    </div>
  </div>

  <table class="grid">
    <colgroup><col style="width:103px"><col style="width:450px"><col style="width:100px"><col style="width:105px"><col style="width:115px"><col style="width:112px"><col style="width:111px"></colgroup>
    <thead>
      <tr><th>Date</th><th>Description</th><th>Class</th><th>Client Name</th><th>Project Name</th><th>Amount</th><th style="padding-left:30px"><span class="check"></span></th></tr>
    </thead>
    <tbody>
      <tr>
        <td style="padding-top:33px"><span class="btn btn-date">Add Date</span><span class="box date-box"></span></td>
        <td class="desc" style="padding:0">
          <h2>Travel</h2>
          <span class="f" style="left:5px;top:36px">From Place</span>
          <span class="box f" style="left:80px;top:34px;width:133px;height:21px"></span>
          <span class="f" style="left:258px;top:36px">To</span>
          <span class="box f" style="left:286px;top:34px;width:133px;height:21px"></span>
          <span class="f" style="left:34px;top:64px">Return</span>
          <span class="check f" style="left:80px;top:64px"></span>
          <span class="f" style="left:103px;top:64px">Method</span>
          <span class="mini-select f" style="left:154px;top:62px;width:56px">Bus</span>
          <span class="f" style="left:236px;top:64px">Payment Method</span>
          <span class="mini-select f" style="left:343px;top:62px;width:76px">None</span>
          <span class="f" style="left:34px;top:98px">Notes</span>
          <span class="box f" style="left:80px;top:96px;width:76px;height:21px"></span>
          <span class="f" style="left:166px;top:98px">Upload</span>
          <span class="box f" style="left:221px;top:96px;width:110px;height:21px"></span>
          <span class="browse f" style="left:335px;top:95px">Browse...</span>
        </td>
        <td style="padding-left:11px"><span class="mini-select" style="width:76px">None</span></td>
        <td style="padding-left:13px"><span class="mini-select" style="width:76px">None</span></td>
        <td style="padding-left:14px"><span class="mini-select" style="width:76px">None</span></td>
        <td style="padding-left:16px"><span class="mini-select" style="width:76px">None</span></td>
        <td style="padding-top:34px"><span class="btn btn-save">Save</span><span class="btn btn-cancel">Cancel</span></td>
      </tr>
    </tbody>
  </table>

  <footer>
    <div class="footer-links">Privacy Policy &nbsp;|&nbsp; Terms &amp; Conditions<br>© 2012, All Rights Reserved</div>
    <div class="follow">Follow Us:</div>
    <span class="social" style="left:999px" aria-label="Social link"></span>
    <span class="social" style="left:1046px" aria-label="Social link"></span>
    <span class="social" style="left:1095px" aria-label="Social link"></span>
  </footer>
</body>
</html>
```